Need Business Cards for my Business

email address: klmvertexcalibration@mailcove.com
web address: klmvertexcalibration.com
Slogan: We offer various NRB licenses
Wallace R. Pendry
Please stick with colors of Company Logo
would like the card to be more of the color example of the logo.
If you need PDF copy of logo email me at the above account.
Creative control rests with you.

Industry/Entity Type

Business

Contact Information for Business Card

I am a minimalist, but would like something to pop and stand out amongst other cards, make it memorable.

Font styles to use
Serif
Decorative
Script

```html
<!DOCTYPE html>
<html lang="en">
<head>
<meta charset="utf-8">
<title>Vertex Calibration Testing – Business Card</title>
<link href="https://fonts.googleapis.com/css2?family=Libre+Baskerville:wght@400;700&family=Montserrat:wght@400;600;700&display=swap" rel="stylesheet">
<style>
  :root {
    --navy: #1b3f73;
    --blue: #1f74bb;
    --red: #e0252f;
    --ink: #2a2a2a;
    --card: #ffffff;
    --backdrop: #e9eaec;
  }
  * { box-sizing: border-box; margin: 0; padding: 0; }
  html, body {
    width: 1200px; height: 900px; overflow: hidden;
    background: var(--backdrop);
  }
  .canvas { position: relative; width: 1200px; height: 900px; }
  .card {
    position: absolute; left: 280px;
    width: 640px; height: 366px;
    background: var(--card);
    border-radius: 22px;
    box-shadow: 0 6px 18px rgba(0,0,0,0.12);
    overflow: hidden;
  }
  .card--front { top: 56px; }
  .card--back { top: 478px; }

  .brand-mark { flex: none; background: var(--red); }
  .brand-name {
    font-family: "Montserrat", sans-serif; font-weight: 700;
    color: var(--navy); letter-spacing: 0.5px; white-space: nowrap;
  }

  /* Front */
  .front-brand {
    position: absolute; left: 0; right: 0; top: 120px;
    display: flex; align-items: center; justify-content: center; gap: 14px;
  }
  .front-brand .brand-mark { width: 18px; height: 18px; }
  .front-brand .brand-name { font-size: 28px; }
  .slogan {
    position: absolute; left: 0; right: 0; bottom: 58px;
    text-align: center;
    font-family: "Libre Baskerville", serif; font-size: 18px;
    letter-spacing: 1.5px; color: var(--navy); text-transform: uppercase;
  }

  /* Back */
  .band {
    position: absolute; left: 0; right: 0; top: 96px; height: 42px;
    background: var(--red);
  }
  .name-tab {
    position: absolute; left: 130px; top: 84px;
    width: 330px; height: 66px;
    background: var(--blue);
    border: 3px solid #fff;
    border-radius: 12px;
    display: flex; align-items: center; justify-content: center;
  }
  .person-name {
    font-family: "Libre Baskerville", serif; font-size: 24px; color: #fff;
    white-space: nowrap;
  }
  .back-brand {
    position: absolute; left: 0; right: 0; top: 178px;
    display: flex; align-items: center; justify-content: center; gap: 12px;
  }
  .back-brand .brand-mark { width: 14px; height: 14px; }
  .back-brand .brand-name { font-size: 24px; }
  .contact {
    position: absolute; left: 0; right: 0; top: 232px;
    text-align: center;
    font-family: "Montserrat", sans-serif; font-size: 15px;
    color: var(--ink); line-height: 1.45;
  }
  .contact-icons {
    display: flex; justify-content: center; gap: 8px; margin-bottom: 6px;
  }
  .contact-icons svg { width: 14px; height: 14px; }
</style>
</head>
<body>
<main class="canvas">

  <section class="card card--front">
    <div class="front-brand">
      <span class="brand-mark"></span>
      <span class="brand-name">Vertex Calibration Testing</span>
    </div>
    <p class="slogan">We offer various NRB licenses</p>
  </section>

  <section class="card card--back">
    <div class="band"></div>
    <div class="name-tab"><span class="person-name">Wallace R. Pendry</span></div>

    <div class="back-brand">
      <span class="brand-mark"></span>
      <span class="brand-name">Vertex Calibration Testing</span>
    </div>

    <div class="contact">
      <div class="contact-icons">
        <svg viewBox="0 0 16 16" aria-label="phone"><path d="M4 1.5l2.2 2.6-1.3 1.7c.9 2 2.4 3.5 4.4 4.4l1.7-1.3 2.6 2.2-1.4 2.4C7.5 13.3 2.7 8.5 1.6 2.9z" fill="var(--blue)"/></svg>
        <svg viewBox="0 0 16 16" aria-label="email"><rect x="1.5" y="3.5" width="13" height="9" rx="1.5" fill="none" stroke="var(--blue)" stroke-width="1.6"/><path d="M2 4.5l6 4.5 6-4.5" fill="none" stroke="var(--blue)" stroke-width="1.6"/></svg>
        <svg viewBox="0 0 16 16" aria-label="website"><circle cx="8" cy="8" r="6.2" fill="none" stroke="var(--blue)" stroke-width="1.5"/><ellipse cx="8" cy="8" rx="2.6" ry="6.2" fill="none" stroke="var(--blue)" stroke-width="1.2"/><path d="M1.8 8h12.4" stroke="var(--blue)" stroke-width="1.2"/></svg>
      </div>
      <p class="contact-phone">+330 5180-2294</p>
      <p class="contact-email">klmvertexcalibration@mailcove.com</p>
      <p class="contact-web">www.klmvertexcalibration.com</p>
    </div>
  </section>

</main>
</body>
</html>
```